New business card design

I need original, modern, business looking but dzen (minimalistic) looking design.
Also refer to websit trevanix.ru

Text is

Дробышев Кирилл, PMP
Партнер

Моб. +7 (915) 460 7185
info@trevanix.ru
Москва, Россия, 117342, ул. Береговая 7/2
=====================

Drobyshev Kirill, PMP
Partner

Mob. +7 (915) 460 7185
info@trevanix.ru
Moscow, Russia,117342, Beregovaya 7/2

Industry/Entity Type

Business

Font styles to use
Serif
Sans Serif

```html
<!DOCTYPE html>
<html lang="en">
<head>
<meta charset="utf-8">
<title>Trevanix — business card</title>
<link rel="stylesheet" href="https://fonts.googleapis.com/css2?family=Oswald:wght@500&family=Roboto+Condensed:wght@300;400&display=swap">
<style>
  :root {
    --stage: #2b2c2e;
    --paper: #ffffff;
    --ink: #3a3a3c;
    --ink-soft: #6b6d70;
    --brand: #2b86cf;
    --brand-light: #5cc3ea;
    --band-shadow: #45474a;
  }
  * { box-sizing: border-box; margin: 0; padding: 0; }
  html, body {
    width: 1200px; height: 864px; overflow: hidden;
    background: var(--stage);
  }
  .canvas { position: relative; width: 1200px; height: 864px; }

  .card {
    position: absolute; width: 620px; height: 354px;
    background: var(--paper);
    box-shadow: 0 10px 30px rgba(0,0,0,.45);
    overflow: hidden;
  }
  .card--front { left: 70px; top: 60px; }
  .card--back  { left: 510px; top: 440px; }

  .wordmark {
    display: flex; align-items: center; gap: 12px;
    font-family: "Roboto Condensed", Arial, sans-serif;
    font-weight: 300; color: var(--brand);
    letter-spacing: .5px; white-space: nowrap;
  }
  .wordmark__mark { background: var(--brand-light); border-radius: 4px; }
  .card--front .wordmark {
    position: absolute; left: 50%; top: 50%;
    transform: translate(-50%, -50%);
    font-size: 48px;
  }
  .card--front .wordmark__mark { width: 46px; height: 46px; }

  .card--back .wordmark {
    position: absolute; right: 34px; top: 52px;
    font-size: 42px;
  }
  .card--back .wordmark__mark { width: 40px; height: 40px; }

  .card__band { position: absolute; inset: 0; }

  .holder { position: absolute; left: 36px; top: 150px; }
  .holder__name {
    font-family: "Oswald", "Arial Narrow", sans-serif;
    font-weight: 500; font-size: 25px; color: var(--ink);
    letter-spacing: .5px; line-height: 1; white-space: nowrap;
  }
  .holder__role {
    margin-top: 5px;
    font-family: "Roboto Condensed", Arial, sans-serif;
    font-size: 12px; letter-spacing: 1.2px; color: var(--ink-soft);
    text-transform: uppercase;
  }

  .contacts {
    position: absolute; left: 36px; top: 222px;
    list-style: none;
    font-family: "Roboto Condensed", Arial, sans-serif;
    font-weight: 300; font-size: 11.5px; color: var(--ink);
  }
  .contacts li { display: flex; align-items: center; gap: 8px; height: 19px; white-space: nowrap; }
  .contacts svg { width: 11px; height: 11px; fill: var(--brand); flex: none; }

  .address {
    position: absolute; right: 30px; top: 272px;
    font-family: "Roboto Condensed", Arial, sans-serif;
    font-size: 15px; color: var(--paper); letter-spacing: .4px;
    white-space: nowrap;
  }
</style>
</head>
<body>
<main class="canvas">

  <section class="card card--front" aria-label="Card front">
    <div class="wordmark"><span class="wordmark__mark"></span>Trevanix</div>
  </section>

  <section class="card card--back" aria-label="Card back">
    <svg class="card__band" viewBox="0 0 620 354" width="620" height="354" aria-hidden="true">
      <path fill="var(--band-shadow)" d="M0 354 V328 H205 C230 328 230 290 247 258 C254 246 262 242 277 242 H620 V354 Z"/>
      <path fill="var(--brand)" d="M0 354 V336 H215 C240 336 240 298 257 266 C264 254 272 250 287 250 H620 V354 Z"/>
    </svg>

    <div class="wordmark"><span class="wordmark__mark"></span>Trevanix</div>

    <div class="holder">
      <p class="holder__name">TOMAS ORLEVIN</p>
      <p class="holder__role">Partner</p>
    </div>

    <ul class="contacts">
      <li><svg viewBox="0 0 12 12"><path d="M2 1h2.5l1 3-1.5 1a7 7 0 0 0 3 3l1-1.5 3 1V10a1 1 0 0 1-1 1A9.5 9.5 0 0 1 1 2a1 1 0 0 1 1-1z"/></svg>+7 (900) 000 0000</li>
      <li><svg viewBox="0 0 12 12"><path d="M3.5 0h5a1 1 0 0 1 1 1v10a1 1 0 0 1-1 1h-5a1 1 0 0 1-1-1V1a1 1 0 0 1 1-1zm0 1.5v8h5v-8z"/></svg>+7 (900) 000 0000</li>
      <li><svg viewBox="0 0 12 12"><path d="M0 2h12v8H0zm1 1 5 3.5L11 3z" fill-rule="evenodd"/></svg>info@trevanix.ru</li>
      <li><svg viewBox="0 0 12 12"><circle cx="6" cy="6" r="6"/></svg>trevanix.ru</li>
    </ul>

    <p class="address">000000, Orlevskaya 1</p>
  </section>

</main>
</body>
</html>
```